Website Design for a Project Management Consulting Business

I have a logo design already and now I need a website.
I am a project manager and run my own consulting business.
Currently I am under contract with 3 major Kestrelmark 300 companies. I'd like a website I can direct current and future clients.
My job is running IT projects and working with developers to deliver business priorities.
The website should be professional and clean - I work IT projects and would like to incorporate that into any theme.
I'd like the site to have several page or breakoff links - sections would include : about me, about my services, a page to display all of my certification badges, another page to talk about highlights from past projects and so on.
Looking for a collaborative experience.

Industry/Entity Type

Kestrelmark 300 Consulting Firm - Project Management

Coding

Coded - Design and coding required

Number of Pages Required

1 page

Font styles to use
Serif

Colors
0094D4
00A9DD
6FCCEA
C7EBF8
E9F6FB
EE7325
F08F49
F5BC92
FAE3D3
FDF4ED

Requirements
Must have
• Sections that are a must: About Me (bio), About My Services, About my Certifications and Credentials, Experience on Past Projects,
Nice to have
• I have added the logo below - I'd like to use the logo and have it prominent ; should be professional and inviting

```html
<!DOCTYPE html>
<html lang="en">
<head>
<meta charset="utf-8">
<title>Keelhaven Projects — IT Project Management</title>
<link href="https://fonts.googleapis.com/css2?family=Inter:wght@400;500;600;700;800&display=swap" rel="stylesheet">
<style>
:root{
  --navy:#032d60;
  --nav-text:#0c3360;
  --blue:#0094D4;
  --sky:#E9F6FB;
  --orange:#EE7325;
  --muted:#5c7fa8;
  --purple:#4b2e8f;
  --ink:#16161f;
  --footer:#1a1a26;
  --white:#ffffff;
}
*{margin:0;padding:0;box-sizing:border-box}
html,body{width:985px;height:1200px;overflow:hidden}
body{position:relative;font-family:"Inter",sans-serif;background:var(--sky);color:var(--navy)}
.abs{position:absolute}

/* header */
.site-header{left:0;top:0;width:985px;height:82px;background:var(--white)}
.header-rule{left:0;top:49px;width:985px;height:1px;background:#e6e9ee}
.brand{display:flex;align-items:center;gap:6px;font-weight:700;color:var(--navy);letter-spacing:.5px}
.brand-mark{width:18px;height:18px;border:2.5px solid var(--navy)}
.brand-name{font-size:13px}
.header-brand{left:152px;top:15px}
.contact-item{font-size:8.5px;line-height:10.5px;color:var(--ink)}
.contact-icon{width:13px;height:13px}
.nav{top:60px;left:0;width:985px;height:12px;font-size:8.5px;letter-spacing:.2px}
.nav a{position:absolute;color:var(--nav-text);text-decoration:none;top:0}
.nav a.active{color:var(--blue)}
.nav .sep{position:absolute;top:2px;width:1px;height:10px;background:var(--nav-text)}

/* hero */
.hero-panel{left:151px;top:108px;width:578px;height:328px;background:var(--navy)}
.hero-accent{left:645px;top:167px;width:204px;height:217px;background:var(--orange)}
.hero-photo{left:565px;top:188px;width:263px;height:298px;background:radial-gradient(ellipse at 45% 40%,#6b4a3a 0%,#3a2a25 35%,#161414 70%,#0d0d0e 100%)}
.hero-title{left:186px;top:180px;width:380px;font-size:30px;line-height:37px;font-weight:400;color:var(--white)}
.hero-sub{left:186px;top:295px;font-size:12.5px;line-height:16.5px;color:#d8e3f0}
.btn-primary{left:188px;top:338px;width:82px;height:26px;background:var(--orange);color:var(--white);font-size:8.5px;font-weight:500;display:flex;align-items:center;justify-content:center;border-radius:1px}

/* credentials */
.badge-row{left:151px;top:452px}
.cert-doc{background:var(--white);padding:4px;box-shadow:0 0 0 1px #e3ebf2}
.cert-doc .fill{width:100%;height:100%}
.cert-one{left:151px;top:531px;width:268px;height:214px}
.cert-one .fill{background:linear-gradient(180deg,#2a64ad 0%,#2a64ad 22%,#f7f9fc 23%,#ffffff 90%,#f2b84b 100%)}
.cert-two{left:566px;top:642px;width:266px;height:206px;padding:0}
.cert-two .fill{background:linear-gradient(135deg,#c9d4dc 0%,#ffffff 30%,#ffffff 78%,#c9d4dc 100%)}
.highlight h3{font-size:12.5px;font-weight:600;color:var(--navy);margin-bottom:5px}
.highlight p{font-size:8.5px;line-height:12.5px;color:var(--muted)}
.highlight-right{left:566px;top:549px;width:270px}
.highlight-left{left:156px;top:786px;width:265px;text-align:right}

/* contact band */
.talk-band{left:0;top:872px;width:985px;height:122px;background:var(--blue)}
.talk-title{left:220px;top:902px;font-size:32px;font-weight:800;color:var(--white);letter-spacing:-.3px}
.talk-sub{left:220px;top:938px;font-size:8.5px;line-height:12.5px;color:#e3f3fb}
.field{background:var(--white);border-radius:1px;font-size:7px;color:#9aa3ad;padding:5px 5px}
.field-details{left:424px;top:911px;width:172px;height:53px}
.field-name{left:607px;top:911px;width:107px;height:24px;padding-top:8px}
.field-email{left:607px;top:940px;width:107px;height:24px;padding-top:8px}
.btn-submit{left:725px;top:940px;width:108px;height:24px;background:var(--ink);color:var(--white);font-size:7px;font-weight:600;display:flex;align-items:center;justify-content:center;border-radius:1px}

/* footer */
.site-footer{left:0;top:994px;width:985px;height:206px;background:var(--footer)}
.footer-brand{left:151px;top:1065px;width:161px;height:27px;background:var(--white);justify-content:center}
.footer-brand .brand-name{font-size:11px}
.footer-brand .brand-mark{width:14px;height:14px;border-width:2px}
.copyright{left:151px;top:1104px;font-size:8.5px;line-height:12.5px;color:#e9ebf0}
.copyright span{color:var(--blue)}
.footer-links{font-size:8.5px;line-height:16.5px;color:#e9ebf0;list-style:none}
</style>
</head>
<body>

<header class="abs site-header">
  <div class="abs brand header-brand"><span class="brand-mark"></span><span class="brand-name">KEELHAVEN PROJECTS</span></div>

  <svg class="abs contact-icon" style="left:459px;top:17px" viewBox="0 0 14 14" fill="none" stroke="#0094D4" stroke-width="1"><path d="M7 13s-4.5-4.3-4.5-7.5a4.5 4.5 0 0 1 9 0C11.5 8.7 7 13 7 13z"/><circle cx="7" cy="5.5" r="1.6"/></svg>
  <div class="abs contact-item" style="left:479px;top:15px">418 Harrow Lane<br>Millbrook, Ohio 44012</div>

  <svg class="abs contact-icon" style="left:597px;top:17px;width:16px" viewBox="0 0 16 13" fill="none" stroke="#0094D4" stroke-width="1"><rect x="0.5" y="1" width="15" height="11" rx="2"/><path d="M2 3l6 4.5L14 3"/></svg>
  <div class="abs contact-item" style="left:618px;top:15px">mara.quell@example.com<br>mara.quell@example.com</div>

  <svg class="abs contact-icon" style="left:751px;top:16px;width:15px;height:15px" viewBox="0 0 16 16" fill="none" stroke="#0094D4" stroke-width="1"><path d="M3.5 1.5l2.5 3-1.5 1.8a9 9 0 0 0 5 5l1.8-1.5 3 2.5-1.6 2.2C8 14 2 8 1.3 3.1z"/><path d="M10 1.5a4.5 4.5 0 0 1 4.5 4.5M10 4a2 2 0 0 1 2 2"/></svg>
  <div class="abs contact-item" style="left:772px;top:15px">(312) 555-0184<br>(312) 555-0193</div>

  <div class="abs header-rule"></div>

  <nav class="abs nav">
    <a class="active" style="left:261px">HOME</a>
    <span class="sep" style="left:306px"></span>
    <a style="left:327px">ABOUT US</a>
    <span class="sep" style="left:390px"></span>
    <a style="left:411px">SERVICES</a>
    <span class="sep" style="left:470px"></span>
    <a style="left:491px">CERTIFICATIONS AND CREDENTIALS</a>
    <span class="sep" style="left:658px"></span>
    <a style="left:678px">CONTACTS</a>
  </nav>
</header>

<section class="hero">
  <div class="abs hero-panel"></div>
  <div class="abs hero-accent"></div>
  <div class="abs hero-photo" role="img" aria-label="Portrait of the consultant in a pinstripe suit on a dark background"></div>
  <h1 class="abs hero-title">IT Projects And Working With Developers To Deliver Business Priorities</h1>
  <svg class="abs" style="left:192px;top:208px" width="132" height="18" viewBox="0 0 132 18" fill="none"><path d="M2 7C40 0 95 3 128 15" stroke="#EE7325" stroke-width="2" stroke-linecap="round"/></svg>
  <p class="abs hero-sub">Currently I Am Under Contract<br>With 3 Major Kestrelmark 300 Companies.</p>
  <a class="abs btn-primary">Get In Touch</a>
</section>

<section class="credentials">
  <svg class="abs badge-row" width="350" height="64" viewBox="0 0 350 64" role="img" aria-label="Certification badges">
    <polygon points="32,1 63,32 32,63 1,32" fill="#1f3559"/>
    <polygon points="32,8 56,32 32,56 8,32" fill="none" stroke="#ffffff" stroke-width="1.5"/>
    <polygon points="125,1 156,32 125,63 94,32" fill="#1f3559"/>
    <polygon points="125,8 149,32 125,56 101,32" fill="none" stroke="#ffffff" stroke-width="1.5"/>
    <circle cx="218" cy="32" r="29" fill="#ffffff" stroke="#4b2e8f" stroke-width="4"/>
    <circle cx="311" cy="32" r="29" fill="#ffffff" stroke="#4b2e8f" stroke-width="4"/>
  </svg>

  <div class="abs cert-doc cert-one"><div class="fill" role="img" aria-label="Agile practitioner certificate document"></div></div>
  <div class="abs cert-doc cert-two"><div class="fill" role="img" aria-label="Product owner certificate document with seal"></div></div>

  <svg class="abs" style="left:420px;top:540px" width="150" height="275" viewBox="420 540 150 275" fill="none" stroke="#6f8fb0" stroke-width="1" stroke-dasharray="5 5">
    <circle cx="431" cy="648" r="2.5" fill="#6f8fb0" stroke="none"/>
    <path d="M434 648H476Q490 648 490 634V571Q490 557 504 557H550"/>
    <path d="M557 557l-5 -3v6z" fill="#6f8fb0" stroke="none"/>
    <circle cx="557" cy="703" r="2.5" fill="#6f8fb0" stroke="none"/>
    <path d="M554 703H512Q498 703 498 717V780Q498 794 484 794H440"/>
    <path d="M432 794l5 -3v6z" fill="#6f8fb0" stroke="none"/>
  </svg>

  <div class="abs highlight highlight-right">
    <h3>Certified Lattice Agile Lead</h3>
    <p>Amet Minim Mollit Non Deserunt Ullamco Est Sit Aliqua Dolor Do Amet Sint. Velit Officia Consequat Duis Enim Velit Mollit. Exercitation Veniam Consequat Sunt Nostrud Amet.</p>
  </div>
  <div class="abs highlight highlight-left">
    <h3>Jordan Ellery</h3>
    <p>Amet Minim Mollit Non Deserunt Ullamco Est Sit Aliqua Dolor Do Amet Sint. Velit Officia Consequat Duis Enim Velit Mollit. Exercitation Veniam Consequat Sunt Nostrud Amet.</p>
  </div>
</section>

<section class="contact">
  <div class="abs talk-band"></div>
  <h2 class="abs talk-title">Let’s Talk!</h2>
  <p class="abs talk-sub">Please Fill In Your Details Below, And Our<br>Advisors Will Give You A Call.</p>
  <div class="abs field field-details">Project Details</div>
  <div class="abs field field-name">Name</div>
  <div class="abs field field-email">E-mails</div>
  <div class="abs btn-submit">Submit</div>
</section>

<footer>
  <div class="abs site-footer"></div>
  <div class="abs brand footer-brand"><span class="brand-mark"></span><span class="brand-name">KEELHAVEN PROJECTS</span></div>
  <p class="abs copyright">© 2022 Consulting Website<br>By <span>Studio Vantor</span></p>
  <ul class="abs footer-links" style="left:704px;top:1056px">
    <li>About</li><li>News</li><li>Contacts</li><li>Testimonials</li><li>Typography</li>
  </ul>
  <ul class="abs footer-links" style="left:769px;top:1056px">
    <li>Services</li><li>Careers</li><li>Our Team</li><li>Shop</li><li>Partners</li>
  </ul>
</footer>

</body>
</html>
```